Double Sided Business Card Design for Pet Services

My mom and I want to start a business for pets. We want to offer dog walking, pet sitting as well as boarding and grooming at our home. For the front of the business card, we want a logo that will capture all of our services. We want the name to be Bigotes, Inc., which means little paws in Spanish. Perhaps, there could be little paws or just a little paw implemented within the word Bigotes. Or we would want a cat and a dog by the word Bigotes. We have a cat and a dog at home, and we would be really happy if they could be a part of the business card. It does not have to be anything crazy. Just an outline of a cat or a dog would be awesome. Please see uploaded file.
As for the back of the card, we would want little paws all over the card or we would want a collar, leash, grooming scissor, dog/cat bowl, bone, fish, or toy to show all of the services that we provide. Along with either the many paws or many pet objects, we would want to add our information, such as name (Lorenza Mireles), telephone numbers (555) 812-3762, e-mail addresses bigotesinc@correomail.net, etc.
We would also want a catch phrase to go on the back of the card, such as "Where all paws matter!" Or "We strive for happy tails." or "A paw-bulous service is guaranteed!"
As for colors, we would not want that many. We would want perhaps white and blue. We would want soft colors that will stand out and make an impression. The same goes with the text. An elegant text would be nice. Or perhaps a text with bold letters. We are excited to see the results, but we are also excited to see your creative ideas and what you will bring to the table.

Target Market(s)

Pet Owners

Contact Information for Business Card

For the front of the business card, we want a logo that will capture all of our services. We want the name to be Bigotes, Inc., which means little paws in Spanish. Perhaps, there could be little paws or just a little paw implemented within the word Bigotes. Or we would want a cat and a dog by the word Bigotes. We have a cat and a dog at home, and we would be really happy if they could be a part of the business card. It does not have to be anything crazy. Just an outline of a cat or a dog would be awesome. Please see uploaded file.
As for the back of the card, we would want little paws all over the card or we would want a collar, leash, grooming scissor, dog/cat bowl, bone, fish, or toy to show all of the services that we provide. Along with either the many paws or many pet objects, we would want to add our information, such as name, telephone numbers, e-mail addresses, etc. We would also want a catch phrase to go on the back of the card, such as "Where all paws matter!" Or "We strive happy tails." or "A paw-bulous service is guaranteed!" Or if there is a way to put the catch phrase in the front of the card. We are open to seeing variety.

Logo Text

Bigotes, Inc

Font styles to use
Serif
Script

Colors
ffffff
33a6d7
145ea8

Requirements
Must have
• My project must be a double sided business card.

```html
<!DOCTYPE html>
<html lang="en">
<head>
<meta charset="utf-8">
<title>Bigotes, Inc – Business Card</title>
<link rel="stylesheet" href="https://fonts.googleapis.com/css2?family=Tinos:wght@400;700&family=Dancing+Script:wght@600&family=Pacifico&display=swap">
<style>
  :root {
    --navy: #0f4c7c;
    --navy-deep: #0b3d66;
    --sky: #33a6d7;
    --coral: #f0907a;
    --teal: #3cb8a6;
    --paper: #ffffff;
    --ink: #1c1c1c;
    --pattern-grey: #e6e8ea;
    --stage: #e9ecef;
  }
  * { box-sizing: border-box; margin: 0; padding: 0; }
  html, body { width: 1200px; height: 912px; overflow: hidden; }
  body { background: var(--stage); position: relative; font-family: "Tinos", "Times New Roman", serif; }

  .card {
    position: absolute; left: 250px; width: 700px; height: 400px;
    border-radius: 22px; overflow: hidden;
    box-shadow: 0 6px 18px rgba(0,0,0,.18);
  }
  .card--front { top: 36px; background: var(--navy); }
  .card--back { top: 476px; background: var(--paper); }

  .pattern { position: absolute; inset: 0; }
  .card--front .pattern { background: linear-gradient(135deg, #155a8e 0%, var(--navy) 55%, var(--navy-deep) 100%); }
  .card--back .pattern { background: linear-gradient(135deg, #f6f7f8 0%, var(--pattern-grey) 100%); opacity: .7; }

  .brand {
    position: absolute; left: 0; right: 0; top: 150px;
    display: flex; align-items: center; justify-content: center; gap: 18px;
  }
  .brand__dot { width: 34px; height: 34px; border-radius: 50%; background: var(--coral); }
  .brand__name { font-family: "Pacifico", cursive; font-size: 58px; color: var(--paper); line-height: 1; }

  .contact {
    position: absolute; right: 34px; top: 22px; text-align: right;
    font-size: 16px; line-height: 20px; color: var(--ink);
  }
  .contact__row { display: flex; justify-content: flex-end; align-items: center; gap: 8px; }
  .contact__icon { width: 16px; height: 16px; border-radius: 50%; background: var(--teal); display: inline-flex; align-items: center; justify-content: center; }
  .contact__address { padding-right: 24px; }

  .person { position: absolute; left: 40px; top: 104px; color: var(--ink); }
  .person__name { font-weight: 700; font-size: 25px; line-height: 30px; margin-bottom: 2px; }
  .person__line { font-size: 15px; line-height: 17px; }

  .divider { position: absolute; left: 40px; right: 40px; top: 208px; height: 1px; background: var(--navy); }

  .services { position: absolute; font-size: 16px; line-height: 24px; color: var(--ink); list-style: none; }
  .services li { display: flex; align-items: center; gap: 8px; }
  .services .mark { width: 10px; height: 10px; border-radius: 50%; }
  .mark--coral { background: var(--coral); }
  .mark--teal { background: var(--teal); }
  .services--left { left: 44px; top: 216px; }
  .services--middle { left: 270px; top: 216px; }
  .services--right { left: 530px; top: 216px; }

  .swoosh { position: absolute; inset: 0; }
  .tagline {
    position: absolute; left: 90px; top: 350px;
    font-family: "Dancing Script", cursive; font-size: 28px; line-height: 1; color: var(--paper);
    transform: rotate(-3deg); transform-origin: left center; white-space: nowrap;
  }
</style>
</head>
<body>

  <section class="card card--front" aria-label="Card front">
    <div class="pattern" role="img" aria-label="Faint repeating pattern of pet items: paws, bones, bowls, collars, scissors and dog houses"></div>
    <div class="brand">
      <span class="brand__dot"></span>
      <span class="brand__name">Bigotes, Inc</span>
    </div>
  </section>

  <section class="card card--back" aria-label="Card back">
    <div class="pattern" role="img" aria-label="Faint grey repeating pattern of pets and pet supplies"></div>

    <svg class="swoosh" width="700" height="400" viewBox="0 0 700 400" aria-hidden="true">
      <path d="M0 328 C250 316 480 292 700 270 L700 282 C480 304 250 328 0 338 Z" fill="var(--coral)"/>
      <path d="M0 344 C250 334 480 310 700 288 L700 400 L0 400 Z" fill="var(--navy)"/>
    </svg>

    <div class="contact">
      <div class="contact__row">(555) 812-3762
        <span class="contact__icon"><svg width="9" height="9" viewBox="0 0 10 10"><path d="M2 1 L4 1 L4.6 3 L3.4 3.8 Q4.4 5.8 6.2 6.6 L7 5.4 L9 6 L9 8 Q5 9 1 2 Z" fill="#fff"/></svg></span>
      </div>
      <div class="contact__row">bigotesinc@correomail.net
        <span class="contact__icon"><svg width="9" height="9" viewBox="0 0 10 10"><rect x="1" y="2.5" width="8" height="5.5" fill="none" stroke="#fff" stroke-width="1.2"/><path d="M1 2.5 L5 5.5 L9 2.5" fill="none" stroke="#fff" stroke-width="1.2"/></svg></span>
      </div>
      <div class="contact__address">214 Linden Lane<br>Harborview, NY 10999</div>
    </div>

    <div class="person">
      <h1 class="person__name">Lorenza Mireles</h1>
      <p class="person__line">Owner</p>
      <p class="person__line">Pet First Aid &amp; CPR Certified</p>
      <p class="person__line">Experienced Veterinary Assistant</p>
      <p class="person__line">Quality TLC</p>
    </div>

    <div class="divider"></div>

    <ul class="services services--left">
      <li><span class="mark mark--coral"></span>Dog Walking</li>
      <li><span class="mark mark--teal"></span>Pet Sitting</li>
    </ul>
    <ul class="services services--middle">
      <li><span class="mark mark--coral"></span>Sleepovers</li>
      <li><span class="mark mark--teal"></span>Medication Administration</li>
    </ul>
    <ul class="services services--right">
      <li><span class="mark mark--coral"></span>Grooming</li>
      <li><span class="mark mark--teal"></span>Boarding</li>
    </ul>

    <p class="tagline">A paw-bulous service is guarenteed!</p>
  </section>

</body>
</html>
```